Business Card Design Project - 2 sided

We need a business card design for a card having one business on each side (ie. two businesses on one card). Would like a design that incorporates logo, tagline and normal fields (name, position, address, phone).

Would also like an allowance for small font text along the bottom (text to be determined, but less than 50 characters).

NB. Attached logo for Verbica Partners has two variations - either can be used.

www.verbicapartners.com / www.kelvarho.com

```html
<!DOCTYPE html>
<html lang="en">
<head>
<meta charset="utf-8">
<title>Verbica Partners / Kelvarho – Business Card</title>
<link rel="stylesheet" href="https://fonts.googleapis.com/css2?family=Open+Sans:wght@400;600;700&display=swap">
<style>
  :root {
    --backdrop: #e9e7e4;
    --paper: #ffffff;
    --navy: #26225e;
    --lime: #8cc63f;
    --sky: #3a8cc9;
    --leaf: #7fb13d;
    --leaf-light: #a3cc56;
    --ink: #3a3a3a;
    --on-dark: #ffffff;
  }
  * { box-sizing: border-box; margin: 0; padding: 0; }
  html, body { width: 1200px; height: 412px; overflow: hidden; }
  body {
    background: var(--backdrop);
    font-family: "Open Sans", Arial, sans-serif;
    position: relative;
  }
  .card {
    position: absolute;
    top: 64px;
    width: 498px;
    height: 284px;
    background: var(--paper);
    overflow: hidden;
    box-shadow: 0 2px 6px rgba(0,0,0,.18);
  }
  .card--verbica { left: 74px; }
  .card--kelvarho { left: 628px; }
  .card__swoosh { position: absolute; inset: 0; width: 100%; height: 100%; }

  .brand { position: absolute; display: flex; align-items: center; gap: 8px; }
  .brand__name { font-weight: 600; line-height: 1; }
  .brand__dot { width: 30px; height: 30px; border-radius: 50%; }
  .tagline { position: absolute; font-size: 9px; color: var(--ink); }

  .card--verbica .brand { left: 34px; top: 92px; }
  .card--verbica .brand__name { font-size: 21px; color: var(--navy); letter-spacing: .5px; }
  .card--verbica .tagline { left: 23px; top: 127px; }

  .card--kelvarho .brand { left: 30px; top: 50px; }
  .card--kelvarho .brand__dot { background: var(--leaf); width: 40px; height: 40px; }
  .card--kelvarho .brand__name { font-size: 36px; color: var(--sky); }
  .card--kelvarho .tagline { left: 70px; top: 98px; font-size: 12.5px; font-weight: 700; color: var(--ink); }

  .person { position: absolute; left: 23px; top: 184px; font-size: 10.5px; color: var(--ink); }
  .person__name { font-size: 14px; font-weight: 700; }
  .card--verbica .person__name { color: var(--navy); }
  .card--kelvarho .person__name { color: var(--sky); }
  .person__sep { margin-left: 2px; }

  .address { position: absolute; left: 23px; top: 234px; font-size: 11.5px; line-height: 17px; color: var(--ink); }

  .contact { position: absolute; right: 12px; top: 160px; list-style: none; text-align: right; color: var(--on-dark); font-size: 11.5px; line-height: 17px; }
  .contact li { display: flex; justify-content: flex-end; align-items: center; gap: 5px; }
  .contact svg { width: 10px; height: 10px; fill: var(--on-dark); }

  .footnote { position: absolute; right: 17px; top: 240px; font-size: 9px; line-height: 13px; color: var(--on-dark); text-align: right; letter-spacing: .2px; }
</style>
</head>
<body>

<section class="card card--verbica" aria-label="Verbica Partners side">
  <svg class="card__swoosh" viewBox="0 0 498 284" preserveAspectRatio="none" aria-hidden="true">
    <path d="M150,284 C300,232 440,120 472,0 L498,0 L498,284 Z" fill="var(--lime)"/>
    <path d="M172,284 C320,244 468,150 498,26 L498,284 Z" fill="var(--navy)"/>
  </svg>
  <div class="brand"><span class="brand__name">Verbica Partners</span></div>
  <p class="tagline">Website Translation and Localisation Specialist...</p>
  <p class="person"><span class="person__name">Your Name</span> <span class="person__sep">/ Title</span></p>
  <p class="address">Complex name, Street name<br>City, State, zip code</p>
  <ul class="contact">
    <li>123-456-7890 <svg viewBox="0 0 10 10"><path d="M2 0.5 L4 2.5 L3 4 Q4.5 6 6 7 L7.5 6 L9.5 8 L8 9.5 Q3 9 0.5 2 Z"/></svg></li>
    <li>123-456-7890 <svg viewBox="0 0 10 10"><rect x="2.5" y="0.5" width="5" height="9" rx="1"/></svg></li>
    <li>123-456-7890 <svg viewBox="0 0 10 10"><rect x="0.5" y="3.5" width="9" height="5" rx="1"/><rect x="2.5" y="0.5" width="5" height="3"/></svg></li>
    <li>name@website.com <svg viewBox="0 0 10 10"><path d="M0.5 2 H9.5 V8.5 H0.5 Z M0.5 2 L5 5.5 L9.5 2" stroke="var(--navy)" stroke-width=".6"/></svg></li>
  </ul>
  <p class="footnote">xxxxxxxxxxxxxxxxxxxxxxxxx<br>xxxxxxxxxxxxxxxxxxxxxxxxx</p>
</section>

<section class="card card--kelvarho" aria-label="Kelvarho side">
  <svg class="card__swoosh" viewBox="0 0 498 284" preserveAspectRatio="none" aria-hidden="true">
    <defs>
      <radialGradient id="leafGlow" cx="0.55" cy="0.7" r="0.6">
        <stop offset="0" stop-color="var(--leaf-light)"/>
        <stop offset="1" stop-color="var(--leaf)"/>
      </radialGradient>
    </defs>
    <path d="M150,284 C300,232 440,120 472,0 L498,0 L498,284 Z" fill="var(--sky)"/>
    <path d="M172,284 C320,244 468,150 498,26 L498,284 Z" fill="url(#leafGlow)"/>
  </svg>
  <div class="brand"><span class="brand__dot"></span><span class="brand__name">Kelvarho</span></div>
  <p class="tagline">Professional SEO Services</p>
  <p class="person"><span class="person__name">Your Name</span> <span class="person__sep">/ Title</span></p>
  <p class="address">Complex name, Street name<br>City, State, zip code</p>
  <ul class="contact">
    <li>123-456-7890 <svg viewBox="0 0 10 10"><path d="M2 0.5 L4 2.5 L3 4 Q4.5 6 6 7 L7.5 6 L9.5 8 L8 9.5 Q3 9 0.5 2 Z"/></svg></li>
    <li>123-456-7890 <svg viewBox="0 0 10 10"><rect x="2.5" y="0.5" width="5" height="9" rx="1"/></svg></li>
    <li>123-456-7890 <svg viewBox="0 0 10 10"><rect x="0.5" y="3.5" width="9" height="5" rx="1"/><rect x="2.5" y="0.5" width="5" height="3"/></svg></li>
    <li>name@website.com <svg viewBox="0 0 10 10"><path d="M0.5 2 H9.5 V8.5 H0.5 Z M0.5 2 L5 5.5 L9.5 2" stroke="var(--leaf)" stroke-width=".6"/></svg></li>
  </ul>
  <p class="footnote">xxxxxxxxxxxxxxxxxxxxxxxxx<br>xxxxxxxxxxxxxxxxxxxxxxxxx</p>
</section>

</body>
</html>
```